Vo Lunec - Business Cards & Stationnery
Think Ahead, Vo Lunec
Professional
Odile Fenwar Quintanel
48 rue des Glycines Doréales
75020 Paris
France
odile@volunec.com
www.volunec.com
The business cards have to be at the european standard ie 8,5 x 5,4 cm (seems to be 3.35'' x 2.13'')
Same for the stationnery ie A4 format, 21 x 29,7 cm (seems to be 8,27'' x 11.7'')
Please use the logo, name of the company and the base line: Think Ahead, Vo Lunec

```html
<!DOCTYPE html>
<html lang="fr">
<head>
<meta charset="utf-8">
<title>Vo Lunec – Carte de visite</title>
<link rel="stylesheet" href="https://fonts.googleapis.com/css2?family=PT+Sans:ital,wght@0,400;0,700;1,700&display=swap">
<style>
  :root {
    --backdrop: #e9e6ea;
    --card-white: #ffffff;
    --violet: #5a2a85;
    --violet-deep: #3d1a60;
    --swoosh: #2b2b2b;
    --swoosh-grey: #9a9a9a;
    --ink: #3a3a3a;
    --text-light: #ffffff;
  }
  * { margin: 0; padding: 0; box-sizing: border-box; }
  html, body {
    width: 1200px; height: 780px; overflow: hidden;
    background: var(--backdrop);
    font-family: "PT Sans", Arial, sans-serif;
  }
  .canvas { position: relative; width: 1200px; height: 780px; }
  .business-card {
    position: absolute; left: 100px; top: 72px;
    width: 1000px; height: 636px;
    border-radius: 26px; overflow: hidden;
    background: var(--card-white);
    box-shadow: 0 6px 22px rgba(0,0,0,0.18);
  }
  .card-shapes { position: absolute; inset: 0; }
  .holder-name {
    position: absolute; right: 58px; top: 40px;
    color: var(--violet); font-weight: 700; font-style: italic;
    font-size: 34px;
  }
  .brand { position: absolute; left: 62px; top: 286px; }
  .brand-line { display: flex; align-items: center; gap: 16px; }
  .brand-mark { width: 34px; height: 34px; background: var(--violet); }
  .brand-name {
    color: var(--ink); font-size: 64px; font-weight: 400;
    letter-spacing: 3px; line-height: 1; text-transform: uppercase;
  }
  .brand-tagline {
    margin-top: 6px; color: var(--ink); font-size: 19px;
    letter-spacing: 3.2px; text-transform: uppercase;
  }
  .address {
    position: absolute; right: 58px; top: 352px;
    color: var(--text-light); text-align: right;
    font-size: 24px; line-height: 1.3; font-style: normal;
  }
  .contact-line { display: flex; justify-content: flex-end; align-items: center; gap: 8px; }
  .contact-row {
    position: absolute; right: 58px; bottom: 36px;
    display: flex; gap: 20px; color: var(--text-light); font-size: 23px;
  }
  .contact-row span { display: flex; align-items: center; gap: 8px; }
  .icon { width: 22px; height: 22px; }
</style>
</head>
<body>
<main class="canvas">
  <section class="business-card" aria-label="Carte de visite Vo Lunec">
    <svg class="card-shapes" viewBox="0 0 1000 636" preserveAspectRatio="none" aria-hidden="true">
      <defs>
        <linearGradient id="violetFill" x1="0" y1="0" x2="1" y2="1">
          <stop offset="0" stop-color="var(--violet)"/>
          <stop offset="1" stop-color="var(--violet-deep)"/>
        </linearGradient>
      </defs>
      <path d="M0,440 C260,430 640,350 1000,92 L1000,150 C640,400 280,478 0,482 Z" fill="var(--swoosh-grey)"/>
      <path d="M0,452 C270,446 650,366 1000,112 L1000,160 C640,410 280,488 0,490 Z" fill="var(--swoosh)"/>
      <path d="M0,490 C280,488 640,410 1000,160 L1000,636 L0,636 Z" fill="url(#violetFill)"/>
    </svg>

    <h1 class="holder-name">Odile Fenwar Quintanel</h1>

    <div class="brand">
      <div class="brand-line">
        <span class="brand-mark" aria-hidden="true"></span>
        <span class="brand-name">Vo Lunec</span>
      </div>
      <p class="brand-tagline">Think Ahead, Vo Lunec</p>
    </div>

    <address class="address">
      48 rue des Glycines Doréales<br>
      75020 Paris, France<br>
      <span class="contact-line">
        <svg class="icon" viewBox="0 0 24 24" aria-hidden="true"><rect x="7" y="2" width="10" height="20" rx="2" fill="none" stroke="#fff" stroke-width="2"/><circle cx="12" cy="18" r="1.3" fill="#fff"/></svg>
        +33 (0)6 47 18 52 30
      </span>
    </address>

    <div class="contact-row">
      <span>
        <svg class="icon" viewBox="0 0 24 24" aria-hidden="true"><rect x="2" y="5" width="20" height="14" fill="#fff"/><path d="M2,5 L12,13 L22,5" fill="none" stroke="var(--violet)" stroke-width="1.8"/></svg>
        odile@volunec.com
      </span>
      <span>
        <svg class="icon" viewBox="0 0 24 24" aria-hidden="true"><circle cx="12" cy="12" r="9" fill="none" stroke="#fff" stroke-width="2"/><ellipse cx="12" cy="12" rx="4" ry="9" fill="none" stroke="#fff" stroke-width="1.5"/><line x1="3" y1="12" x2="21" y2="12" stroke="#fff" stroke-width="1.5"/></svg>
        www.volunec.com
      </span>
    </div>
  </section>
</main>
</body>
</html>
```